Design for an exciting tech startup! Brochure+Letter Design Project

We're a startup called plannixxo with Phase 1 of a super exciting Remote Desk Conductor software and app launching this October (plannixxo.com)

While we've got some basic items such as the corporate identity and website locked down, we're still lacking the essential little communication items that potential customers will be receiving from us.

We need a designer who can bring out a consistency into our stationery both on the online and offline items. We'd also like a recommended graphic style to represent the visuals that will be shown, especially in our user manual eg. icon-based OR flow chart style etc.

The list is as below. We're looking for templates here as the final items will be laid out at a later stage only when all contents are finalised.

1. A4 horizontal, 4-page brochure template
- circulated in PDF
- also allocate space for 2 equal size images per page
- page 1 with a prominent header, page 4 with a prominent footer
- to provide files in AI or PSD format
2. A4 horizontal, 20 page User Manual
- circulated in PDF
- also allocate space for 1 large image and 1 small image per page
3. Electronic direct mailer template
- for maximum of 200 words
4. A4 vertical, Letterhead template
- used in PDF form (potentially for press releases)
- prominent footer

If you are interested, please email us to receive these items:
1. Corporate Identity sheet on logo usage
2. E-direct mailer content

Good luck and enjoy your mission!
Updates

Dear Designers,

This project is mainly a brochure template + adaptation of this template's design to letterhead and electronic mailer.

We've made the brief more precise in case it has caused any misunderstanding and inconveniences to anyone.

Our brand identity items have also been uploaded for your reference.

Good luck!

Target Market(s)

HR and IT managers who will subscribe to the software on behalf of their companies, also bosses of Small Medium enterprises.

Industry/Entity Type

Communication

Requirements
Must have
• We only use these fonts:
Century Gothic
Arial

Currently, our preferred colours are blue and silver though we would not want to be restricted by strictly following these 2 colours.

```html
<!DOCTYPE html>
<html lang="en">
<head>
<meta charset="utf-8">
<title>plannixxo – brochure cover</title>
<link rel="stylesheet" href="https://fonts.googleapis.com/css2?family=Arimo:wght@400;700&display=swap">
<style>
  :root {
    --sky-top: #a9d3ef;
    --sky-mid: #d6eaf8;
    --cloud: #f3f9fd;
    --paper: #ffffff;
    --accent: #2a9ed8;
    --brand: #1a5b93;
    --divider: #4aa7dc;
    --cube-light: #f4f7fa;
    --cube-shade: #c9d6e2;
    --cube-accent: #7fb8e0;
    --motif: #eef1f4;
    --band-start: #1b8ccf;
    --band-end: #3aaae2;
    --band-text: #ffffff;
  }
  * { margin: 0; padding: 0; box-sizing: border-box; }
  html, body {
    width: 1200px;
    height: 848px;
    overflow: hidden;
    background: var(--paper);
  }
  .cover {
    position: relative;
    width: 1200px;
    height: 848px;
    background: var(--paper);
    font-family: "Arimo", Arial, sans-serif;
    overflow: hidden;
  }
  .sky-visual {
    position: absolute;
    left: 0;
    top: 0;
    width: 1200px;
    height: 180px;
    background:
      radial-gradient(ellipse 260px 90px at 520px 60px, var(--cloud) 0%, rgba(243,249,253,0) 100%),
      radial-gradient(ellipse 300px 80px at 860px 40px, var(--cloud) 0%, rgba(243,249,253,0) 100%),
      radial-gradient(ellipse 220px 70px at 160px 30px, var(--cloud) 0%, rgba(243,249,253,0) 100%),
      linear-gradient(180deg, var(--sky-top) 0%, var(--sky-mid) 50%, var(--paper) 100%);
  }
  .cubes-visual {
    position: absolute;
    left: 16px;
    top: 20px;
    width: 226px;
    height: 182px;
    border-radius: 28px;
    background:
      radial-gradient(circle at 65% 55%, var(--cube-accent) 0%, rgba(127,184,224,0) 30%),
      radial-gradient(ellipse at 40% 45%, var(--cube-light) 0%, var(--cube-shade) 100%);
    opacity: 0.75;
  }
  .motif-visual {
    position: absolute;
    left: 800px;
    top: 510px;
    width: 420px;
    height: 300px;
    background: radial-gradient(ellipse at 70% 55%, var(--motif) 0%, rgba(238,241,244,0) 70%);
  }
  .welcome {
    position: absolute;
    right: 644px;
    top: 386px;
    text-align: right;
    color: var(--accent);
    font-size: 29px;
    font-weight: 400;
    letter-spacing: 4.2px;
    line-height: 43px;
  }
  .divider {
    position: absolute;
    left: 601px;
    top: 381px;
    width: 2px;
    height: 94px;
    background: var(--divider);
  }
  .brand-name {
    position: absolute;
    left: 644px;
    top: 378px;
    color: var(--brand);
    font-size: 88px;
    font-weight: 700;
    line-height: 88px;
    letter-spacing: -1px;
  }
  .footer-band {
    position: absolute;
    left: 0;
    bottom: 0;
    width: 1200px;
    height: 56px;
    background: linear-gradient(90deg, var(--band-start) 0%, var(--band-end) 100%);
  }
  .web-address {
    position: absolute;
    right: 37px;
    top: 16px;
    color: var(--band-text);
    font-size: 19px;
    letter-spacing: 5px;
    line-height: 24px;
  }
</style>
</head>
<body>
  <main class="cover">
    <div class="sky-visual" role="img" aria-label="Soft blue sky with light clouds"></div>
    <div class="cubes-visual" role="img" aria-label="Floating white cubes with blue letters"></div>
    <div class="motif-visual" role="img" aria-label="Faint large brand motif in light grey"></div>

    <p class="welcome">welcome to<br>remote desk conductor</p>
    <div class="divider"></div>
    <h1 class="brand-name">plannixxo</h1>

    <footer class="footer-band">
      <p class="web-address">www.plannixxo.com</p>
    </footer>
  </main>
</body>
</html>
```